Travinex - You are the Boss!

Travinex is a new Silicon Valley company, of the pelim founders from Berlin, which provides a "Shared Pioneer Circle". This platform allows the crowd to support startups with money, experts and fame. Our Vision is, that everyone should become an entrepreneur.

Pls find all brief details in the attached document
Updates

Would be nice to have a list of more social services I'm available on, like a list of pictograms of all my services:

Find me on: vooka, bramlet+, qrt, fenwix, moodrail, zupp, hvoxa, etc...

pls make sure to use the right font:
http://www.typemarlow.com/fonts/Velquin

Target Market(s)

Main target market is those already involved in the startup industry, by fundraising, investing, advising, cofounding and working. Travinex brings a totaly new transparency and collaborative way of starting companies to that business.

· Entrepreneurs (looking for funding, team and community)
· Investors (looking for hot investments and )
· Experts (workers looking for startups they can work for equity)
· Incubators & Business Schools (looking for tools to advise startups)

Industry/Entity Type

It Company

Requirements
Must have
• Pls find all brief details in the attached document
Nice to have

```html
<!DOCTYPE html>
<html lang="en">
<head>
<meta charset="utf-8">
<title>Travinex – Business Card</title>
<link href="https://fonts.googleapis.com/css2?family=Orbitron:wght@500;700&family=Open+Sans:wght@400;700&display=swap" rel="stylesheet">
<style>
  :root {
    --stage: #000000;
    --orange-light: #f7941d;
    --orange-mid: #f36f24;
    --orange-deep: #f15a29;
    --card-white: #ffffff;
    --text-dark: #4a4a4a;
    --text-on-orange: #ffffff;
    --watermark: #e8e8e8;
  }
  html, body {
    margin: 0;
    padding: 0;
    width: 1200px;
    height: 1168px;
    overflow: hidden;
    background: var(--stage);
  }
  .canvas {
    position: relative;
    width: 1200px;
    height: 1168px;
    background: var(--stage);
  }
  .card {
    position: absolute;
    border-radius: 28px;
    overflow: hidden;
  }
  .card--front {
    left: 244px;
    top: 142px;
    width: 688px;
    height: 400px;
    background: radial-gradient(ellipse 55% 60% at 50% 45%, var(--orange-light) 0%, var(--orange-mid) 55%, var(--orange-deep) 100%);
    color: var(--text-on-orange);
    text-align: center;
  }
  .brand-name {
    position: absolute;
    left: 0;
    right: 0;
    top: 112px;
    font-family: "Orbitron", sans-serif;
    font-weight: 700;
    font-size: 64px;
    letter-spacing: 2px;
    color: var(--text-on-orange);
  }
  .tagline {
    position: absolute;
    left: 0;
    right: 0;
    top: 226px;
    margin: 0;
    font-family: "Orbitron", sans-serif;
    font-weight: 700;
    font-size: 38px;
    letter-spacing: 1px;
  }
  .invite {
    position: absolute;
    left: 0;
    right: 0;
    top: 310px;
    margin: 0;
    font-family: "Open Sans", sans-serif;
    font-size: 16px;
    line-height: 22px;
  }
  .card--back {
    left: 248px;
    top: 572px;
    width: 690px;
    height: 396px;
    background: var(--card-white);
  }
  .name-band {
    position: absolute;
    left: 0;
    top: 59px;
    width: 597px;
    height: 108px;
    background: linear-gradient(90deg, var(--orange-light) 0%, var(--orange-deep) 100%);
    color: var(--text-on-orange);
  }
  .person-name {
    position: absolute;
    left: 113px;
    top: 14px;
    margin: 0;
    font-family: "Open Sans", sans-serif;
    font-weight: 700;
    font-size: 38px;
  }
  .person-role {
    position: absolute;
    right: 125px;
    top: 64px;
    margin: 0;
    font-family: "Open Sans", sans-serif;
    font-size: 22px;
  }
  .contact-list {
    position: absolute;
    right: 351px;
    top: 244px;
    margin: 0;
    padding: 0;
    list-style: none;
    text-align: right;
    font-family: "Open Sans", sans-serif;
    font-size: 22px;
    line-height: 25px;
    color: var(--text-dark);
  }
  .brand-watermark {
    position: absolute;
    left: 440px;
    top: 220px;
    width: 230px;
    height: 150px;
  }
</style>
</head>
<body>
  <main class="canvas">
    <section class="card card--front">
      <div class="brand-name">Travinex</div>
      <h1 class="tagline">You are the Boss!</h1>
      <p class="invite">Are you interested in Startups, Investments, Work?<br>Join: Friendwall.com/Travinex</p>
    </section>

    <section class="card card--back">
      <div class="name-band">
        <h2 class="person-name">Lukas Brandauer</h2>
        <p class="person-role">Founder and CEO</p>
      </div>
      <ul class="contact-list">
        <li>+44 - 321 - 654 - 987</li>
        <li>the@travinex.com</li>
        <li>chirpnet.com/lukasbrandauer</li>
        <li>friendwall.com/lukasbrandauer</li>
        <li>linkhub.com/in/lukasbrandauer</li>
      </ul>
      <svg class="brand-watermark" viewBox="0 0 230 150" aria-hidden="true">
        <text x="115" y="90" text-anchor="middle" font-family="Orbitron, sans-serif" font-weight="700" font-size="40" fill="var(--watermark)">Travinex</text>
      </svg>
    </section>
  </main>
</body>
</html>
```